Business card for a vending machine business

I need a business card for my vending machine business. The name is Kestrel Snackworks, LLC. The card is one-sided, and landscape format. Not portrait.

The information for the card is as follows:

Dana Whitlow
Owner
(555) 314-2907
Kestrelsnackworks.example
Info@kestrelsnackworks.example

I'd like colors and design elements to match what's in my logo and company name. I'd like to have the checkered flag or racing stripe if possible You can use a border if youd like. You can use a background color if it looks nice and doesn't clash with the logo
Use your creativity. But a white background is perfectly fine. The card can be as simple, yet gets the point across to match the company name and logo.

I uploaded a copy of my logo. I also uploaded a businesses card I started to create, but since it was missing something, I gave up. Another upload has a red thunderbolt and the checkerer flag. Those two uploads are for inspiration. Again, please make sure to make the card landscape, not portrait. Thank you, designers. Good luck to all.

```html
<!DOCTYPE html>
<html lang="en">
<head>
<meta charset="utf-8">
<title>Kestrel Snackworks — Business Card</title>
<link href="https://fonts.googleapis.com/css2?family=Montserrat:wght@400;500;600&display=swap" rel="stylesheet">
<style>
  :root {
    --race-red: #e8161b;
    --ink: #1c1c1c;
    --card-white: #ffffff;
    --card-black: #1e1e1e;
    --backdrop: #4a4a4a;
  }
  * { box-sizing: border-box; margin: 0; padding: 0; }
  html, body { width: 1200px; height: 1200px; overflow: hidden; }
  body {
    background: var(--backdrop);
    font-family: "Montserrat", Arial, sans-serif;
    display: flex;
    flex-direction: column;
    align-items: center;
    justify-content: center;
    gap: 44px;
  }
  .card {
    position: relative;
    width: 900px;
    height: 514px;
    border-radius: 38px;
    overflow: hidden;
    border-bottom: 4px solid var(--race-red);
  }
  .card--front { background: var(--card-white); }
  .card--back { background: var(--card-black); display: flex; align-items: center; justify-content: center; }

  .brand {
    display: flex;
    align-items: center;
    gap: 16px;
    color: var(--race-red);
    font-weight: 600;
    text-transform: uppercase;
    line-height: 1.05;
  }
  .brand__mark { background: var(--race-red); flex: none; }
  .card--front .brand { position: absolute; top: 78px; right: 90px; font-size: 34px; }
  .card--front .brand__mark { width: 26px; height: 26px; }
  .card--back .brand { font-size: 52px; }
  .card--back .brand__mark { width: 40px; height: 40px; }

  .contact { position: absolute; left: 66px; top: 196px; }
  .contact__name { color: var(--race-red); font-size: 40px; font-weight: 600; letter-spacing: 0.5px; }
  .contact__role { color: var(--ink); font-size: 30px; font-weight: 400; margin: 2px 0 14px 32px; }
  .contact__list { list-style: none; margin-left: 32px; }
  .contact__item {
    display: flex; align-items: center; gap: 16px;
    color: var(--ink); font-size: 25px; font-weight: 400; height: 42px;
  }
  .contact__icon { width: 30px; height: 30px; flex: none; }

  .checker-strip {
    position: absolute; left: 0; right: 0; bottom: 0; height: 58px;
    background: linear-gradient(90deg, #f23a3e, var(--race-red));
  }
</style>
</head>
<body>
  <section class="card card--front">
    <div class="brand"><span class="brand__mark"></span><span>Kestrel<br>Snackworks</span></div>

    <div class="contact">
      <p class="contact__name">DANA WHITLOW</p>
      <p class="contact__role">OWNER</p>
      <ul class="contact__list">
        <li class="contact__item">
          <svg class="contact__icon" viewBox="0 0 24 24" aria-hidden="true"><path fill="#e8161b" d="M6.6 10.8a15.1 15.1 0 0 0 6.6 6.6l2.2-2.2a1 1 0 0 1 1-.25 11.4 11.4 0 0 0 3.6.57 1 1 0 0 1 1 1V20a1 1 0 0 1-1 1A17 17 0 0 1 3 4a1 1 0 0 1 1-1h3.5a1 1 0 0 1 1 1c0 1.25.2 2.45.57 3.57a1 1 0 0 1-.25 1z"/></svg>
          (555) 314-2907
        </li>
        <li class="contact__item">
          <svg class="contact__icon" viewBox="0 0 24 24" aria-hidden="true" fill="none" stroke="#e8161b" stroke-width="2"><circle cx="12" cy="12" r="9.5"/><ellipse cx="12" cy="12" rx="4" ry="9.5"/><path d="M2.5 12h19M4 7h16M4 17h16"/></svg>
          Kestrelsnackworks.example
        </li>
        <li class="contact__item">
          <svg class="contact__icon" viewBox="0 0 24 24" aria-hidden="true"><path fill="#e8161b" d="M2 5h20v14H2z"/><path d="M2 5l10 8 10-8" fill="none" stroke="#fff" stroke-width="1.8"/></svg>
          Info@kestrelsnackworks.example
        </li>
      </ul>
    </div>

    <div class="checker-strip" role="img" aria-label="Red and white checkered racing strip"></div>
  </section>

  <section class="card card--back">
    <div class="brand"><span class="brand__mark"></span><span>Kestrel<br>Snackworks</span></div>
  </section>
</body>
</html>
```